Business card to be used as a flyer

This business card should do the trick of a full scale flyer , so basicaly from the business card itself we only keep the size and remove the clasical name , position , company name (etc).
This business cards should be , like said above, used as promo tool, being gived to different girls . So base one : the design is girls oriented.
Colors : black background . We will use gold (color) folio for the text.
Attached you have our logo, but this should not be a proiminent part of the design . You can use only the cat head instead.
Target Market(s)
Girls / Women
Contact Information for Business Card
> black background , gold / folio text and elements
> cat head from the logo in a creative way do be displayed
> proieminent text "your path to success starts here"
> contact details phone and website .
www.velmastrand.ro (website) and 0742163958 (phone)

```html
<!DOCTYPE html>
<html lang="en">
<head>
<meta charset="UTF-8">
<title>Velmastrand – Promo Card</title>
<link rel="stylesheet" href="https://fonts.googleapis.com/css2?family=Pinyon+Script&family=Montserrat:wght@400&display=swap">
<style>
  :root {
    --card-black: #000000;
    --gold-light: #f7dd7a;
    --gold-mid: #d9a93a;
    --gold-deep: #a8761c;
    --gold-text: #e6bd52;
    --text-white: #ffffff;
  }
  html, body {
    margin: 0;
    padding: 0;
    width: 1200px;
    height: 686px;
    overflow: hidden;
    background: var(--card-black);
  }
  .card {
    position: relative;
    width: 1200px;
    height: 686px;
    background: var(--card-black);
    overflow: hidden;
  }
  .headline {
    position: absolute;
    left: 70px;
    top: 78px;
    margin: 0;
    font-family: "Pinyon Script", cursive;
    font-weight: 400;
    font-size: 134px;
    line-height: 129px;
    letter-spacing: 3px;
    white-space: nowrap;
    background: linear-gradient(160deg, var(--gold-light) 0%, var(--gold-mid) 45%, var(--gold-deep) 70%, var(--gold-light) 100%);
    -webkit-background-clip: text;
    background-clip: text;
    color: transparent;
  }
  .headline span { display: block; }
  .cat-artwork {
    position: absolute;
    left: 714px;
    top: 17px;
    width: 486px;
    height: 669px;
    border-radius: 46% 0 0 30%;
    background:
      radial-gradient(ellipse at 60% 40%, rgba(247, 221, 122, 0.55) 0%, rgba(217, 169, 58, 0.45) 35%, rgba(168, 118, 28, 0.30) 65%, rgba(168, 118, 28, 0.12) 100%);
  }
  .contact {
    position: absolute;
    left: 74px;
    top: 614px;
    display: flex;
    align-items: center;
    gap: 86px;
    font-family: "Montserrat", Arial, sans-serif;
    font-size: 23px;
    color: var(--text-white);
  }
  .contact-item {
    display: flex;
    align-items: center;
    gap: 12px;
  }
  .contact-icon {
    width: 35px;
    height: 35px;
    display: block;
  }
</style>
</head>
<body>
  <main class="card">
    <h1 class="headline">
      <span>Your path to</span>
      <span>Success</span>
      <span>Starts here</span>
    </h1>

    <div class="cat-artwork" role="img" aria-label="Gold glitter line illustration of a cat head in profile"></div>

    <div class="contact">
      <div class="contact-item">
        <svg class="contact-icon" viewBox="0 0 34 34" aria-hidden="true">
          <rect x="1" y="1" width="32" height="32" rx="7" fill="none" stroke="var(--gold-text)" stroke-width="1.6"/>
          <path d="M11.5 8.5 l3.2 3.6 -1.8 2.4 c1.2 2.6 3 4.4 5.6 5.6 l2.4 -1.8 3.6 3.2 -1.8 3 c-6.8 -0.4 -12.4 -6 -12.8 -12.8 z" fill="none" stroke="var(--gold-text)" stroke-width="1.6" stroke-linejoin="round"/>
        </svg>
        <span class="contact-text">0742163958</span>
      </div>
      <div class="contact-item">
        <svg class="contact-icon" viewBox="0 0 34 34" aria-hidden="true">
          <rect x="1" y="1" width="32" height="32" rx="7" fill="none" stroke="var(--gold-text)" stroke-width="1.6"/>
          <g fill="none" stroke="var(--gold-text)" stroke-width="1.5">
            <circle cx="17" cy="17" r="9"/>
            <ellipse cx="17" cy="17" rx="4" ry="9"/>
            <line x1="8" y1="17" x2="26" y2="17"/>
            <path d="M9.5 12.5 h15 M9.5 21.5 h15"/>
          </g>
        </svg>
        <span class="contact-text">www.velmastrand.ro</span>
      </div>
    </div>
  </main>
</body>
</html>
```